Brochure for Strucova, will be used to hand out to clients.

Need a design for a company brochure (4 pages including front&back + 2 in the middle that looks professional and sells our engineering capabilities to prospective clients. These clients will be architects, builders and developers.

Instructions
1) Open the brochure concept design PDF documents
2) Refer to photo, word files and PDF add in's
3) Setup the Resume section with photo + description and bullet points which can be filled in later (I will advise in 1 or 2 revisions)

The "Services Integration" PDF graph needs a bit of work to tart it up a bit and then inserted into the noted area.

I consider what I have provided as a guideline (neat laid out doc) however you have the ability to change the design if you think it could be better. Must be 4 pages and contain majority of info I have provided.

Target Market(s)

Architects, developers, builders

Industry/Entity Type

Engineering Consultant

Font styles to use
Serif
Sans Serif

Colors
9bcb3b
abd036
cadf82
eaf2ce
86cfc7
cfeae6
fbf289
fee18a
fbc994

Requirements
Must have
• The Brochure should be 4 x A4 pages which is a printed A3 sheet and then folded in half into a neat document.
• Presents well
Nice to have
• Brochure to be professional, minimalistic in a way but also interesting.
• Company colors are in our logo which is predominately green. Will leave colour scheme to the designer

```html
<!DOCTYPE html>
<html lang="en">
<head>
<meta charset="utf-8">
<title>Strucova Design – Brochure Spread</title>
<link href="https://fonts.googleapis.com/css2?family=Michroma&family=Open+Sans:wght@400;600;700&display=swap" rel="stylesheet">
<style>
:root{
  --green:#8dc03f;
  --green-dark:#6fa52c;
  --green-light:#abd036;
  --green-pale:#eaf2ce;
  --ink:#2b2b2b;
  --grey:#6b6b6b;
  --grey-light:#efefef;
  --stage:#d9d9d9;
  --white:#ffffff;
}
*{box-sizing:border-box;margin:0;padding:0}
html,body{width:1200px;height:824px;overflow:hidden}
body{background:var(--stage);font-family:"Open Sans",Arial,sans-serif;color:var(--ink);position:relative}
.page{position:absolute;top:30px;width:540px;height:764px;background:linear-gradient(160deg,#fff 0%,#f3f3f3 100%);overflow:hidden;box-shadow:0 2px 10px rgba(0,0,0,.15)}
.page--inside{left:60px}
.page--cover{left:600px}

/* inside page */
.team-band{position:absolute;left:0;top:0;width:100%;height:70px;background:linear-gradient(90deg,var(--green-dark),var(--green-light))}
.team-title{position:absolute;left:0;top:24px;width:100%;text-align:center;font-family:"Michroma",sans-serif;font-size:19px;letter-spacing:7px;color:var(--white)}
.profiles{position:absolute;top:86px;left:22px;right:22px;display:flex;justify-content:space-between}
.profile{width:158px}
.profile__photo{width:100px;height:112px;margin:0 auto;background:linear-gradient(180deg,#d8d2cc,#a89a8c)}
.profile__name{background:var(--green);color:var(--white);font-family:"Michroma",sans-serif;font-size:9px;text-align:center;padding:5px 0;margin-top:-4px;position:relative}
.profile__role{font-size:8.5px;text-align:center;color:var(--grey);margin:5px 0}
.profile__bio{background:var(--grey-light);font-size:7.5px;line-height:1.45;color:var(--grey);padding:7px 8px;text-align:center}
.sectors{position:absolute;top:340px;left:22px;right:22px}
.sector-row{display:flex;height:70px}
.sector-col{width:165px}
.sector-tag{display:inline-block;background:var(--green);color:var(--white);font-family:"Michroma",sans-serif;font-size:8.5px;padding:5px 12px;margin-bottom:5px;width:150px}
.ticks{list-style:none;font-size:8.5px;color:var(--grey);line-height:1.5}
.ticks li::before{content:"\2713";color:var(--green);margin-right:5px;font-weight:700}
.sector-col--plain{padding-top:22px}
.contact-band{position:absolute;left:0;top:640px;width:100%;height:38px;background:var(--green);display:flex}
.contact-band__address{flex:1;color:var(--white);font-size:10px;display:flex;align-items:center;padding-left:22px;gap:6px}
.contact-band__links{width:220px;background:var(--green-light);color:var(--white);font-size:9px;display:flex;flex-direction:column;justify-content:center;padding-left:14px;line-height:1.5}
.badges{position:absolute;left:30px;top:698px;display:flex;gap:16px}
.badge{width:40px;height:34px;background:#c9d6e3}
.badge--round{border-radius:50%;background:#d64a4a;width:34px}

/* cover page */
.cover-band{position:absolute;top:0;left:0;width:100%;height:52px;background:linear-gradient(90deg,var(--green-light),var(--green))}
.cover-web{position:absolute;top:20px;width:100%;text-align:center;font-size:11px;letter-spacing:8px;color:var(--white)}
.photo-strip{position:absolute;top:52px;left:0;width:100%;height:220px;display:flex;gap:3px;background:var(--white)}
.photo{flex:1}
.swoosh{position:absolute;top:230px;left:0;width:100%;height:130px}
.brand{position:absolute;top:410px;left:300px;display:flex;align-items:center;gap:10px}
.brand__mark{width:34px;height:34px;background:var(--green)}
.brand__name{font-family:"Michroma",sans-serif;font-size:17px;color:var(--green-dark);line-height:1.25}
.abn{position:absolute;top:480px;left:300px;background:var(--green);color:var(--white);font-family:"Michroma",sans-serif;font-size:10px;padding:7px 22px;border-radius:16px}
.cover-heading{position:absolute;top:540px;left:40px;font-family:"Michroma",sans-serif;color:var(--ink)}
.cover-heading__main{font-size:22px;letter-spacing:1px}
.cover-heading__sub{font-size:13px;margin-top:4px}
.services{position:absolute;top:610px;left:40px;list-style:none;font-family:"Michroma",sans-serif;font-size:9.5px;color:var(--grey);line-height:2}
.services li::before{content:"\00BB";color:var(--green);font-weight:700;margin-right:8px;font-size:13px}
</style>
</head>
<body>

<section class="page page--inside">
  <div class="team-band"></div>
  <h2 class="team-title">OUR SENIOR DESIGN TEAM</h2>

  <div class="profiles">
    <article class="profile">
      <div class="profile__photo" role="img" aria-label="Portrait photo of Daniel Ferrant"></div>
      <div class="profile__name">DANIEL FERRANT</div>
      <p class="profile__role">Mechanical Service Engineer</p>
      <p class="profile__bio">Daniel has over 15 years' experience in building services design, leading mechanical systems for commercial projects with a focus on efficient, practical and buildable engineering outcomes.</p>
    </article>
    <article class="profile">
      <div class="profile__photo" role="img" aria-label="Portrait photo of Colin Ashdown"></div>
      <div class="profile__name">COLIN ASHDOWN</div>
      <p class="profile__role">Hydraulic/Wet Fire Service Engineer</p>
      <p class="profile__bio">Colin has over 12 years' experience in hydraulic and fire services design, delivering compliant, coordinated systems for residential, retail and healthcare projects across the state.</p>
    </article>
    <article class="profile">
      <div class="profile__photo" role="img" aria-label="Portrait photo of Colin Ashdown"></div>
      <div class="profile__name">COLIN ASHDOWN</div>
      <p class="profile__role">Electrical Service Engineer</p>
      <p class="profile__bio">Colin has over 12 years' experience in electrical services design, delivering lighting, power and energy solutions that suit client budgets and long-term building performance.</p>
    </article>
  </div>

  <div class="sectors">
    <div class="sector-row">
      <div class="sector-col"><span class="sector-tag">RESIDENTIAL</span>
        <ul class="ticks"><li>Lorem ipsum dolor sit amet.</li><li>Lorem ipsum dolor sit amet.</li><li>Lorem ipsum dolor sit amet.</li></ul></div>
      <div class="sector-col sector-col--plain"><ul class="ticks"><li>Lorem ipsum dolor sit amet.</li><li>Lorem ipsum dolor sit amet.</li><li>Lorem ipsum dolor sit amet.</li></ul></div>
      <div class="sector-col sector-col--plain"><ul class="ticks"><li>Lorem ipsum dolor sit amet.</li><li>Lorem ipsum dolor sit amet.</li><li>Lorem ipsum dolor sit amet.</li></ul></div>
    </div>
    <div class="sector-row">
      <div class="sector-col"><span class="sector-tag">OFFICES</span>
        <ul class="ticks"><li>Lorem ipsum dolor sit amet.</li><li>Lorem ipsum dolor sit amet.</li><li>Lorem ipsum dolor sit amet.</li></ul></div>
      <div class="sector-col sector-col--plain"><ul class="ticks"><li>Lorem ipsum dolor sit amet.</li><li>Lorem ipsum dolor sit amet.</li><li>Lorem ipsum dolor sit amet.</li></ul></div>
      <div class="sector-col sector-col--plain"><ul class="ticks"><li>Lorem ipsum dolor sit amet.</li><li>Lorem ipsum dolor sit amet.</li><li>Lorem ipsum dolor sit amet.</li></ul></div>
    </div>
    <div class="sector-row">
      <div class="sector-col"><span class="sector-tag">RETAIL/INDUSTRIES</span>
        <ul class="ticks"><li>Lorem ipsum dolor sit amet.</li><li>Lorem ipsum dolor sit amet.</li><li>Lorem ipsum dolor sit amet.</li></ul></div>
      <div class="sector-col sector-col--plain"><ul class="ticks"><li>Lorem ipsum dolor sit amet.</li><li>Lorem ipsum dolor sit amet.</li><li>Lorem ipsum dolor sit amet.</li></ul></div>
      <div class="sector-col sector-col--plain"><ul class="ticks"><li>Lorem ipsum dolor sit amet.</li><li>Lorem ipsum dolor sit amet.</li><li>Lorem ipsum dolor sit amet.</li></ul></div>
    </div>
    <div class="sector-row">
      <div class="sector-col"><span class="sector-tag">HOSPITAL/MEDICAL</span>
        <ul class="ticks"><li>Lorem ipsum dolor sit amet.</li><li>Lorem ipsum dolor sit amet.</li><li>Lorem ipsum dolor sit amet.</li></ul></div>
      <div class="sector-col sector-col--plain"><ul class="ticks"><li>Lorem ipsum dolor sit amet.</li><li>Lorem ipsum dolor sit amet.</li><li>Lorem ipsum dolor sit amet.</li></ul></div>
      <div class="sector-col sector-col--plain"><ul class="ticks"><li>Lorem ipsum dolor sit amet.</li><li>Lorem ipsum dolor sit amet.</li><li>Lorem ipsum dolor sit amet.</li></ul></div>
    </div>
  </div>

  <div class="contact-band">
    <div class="contact-band__address">
      <svg width="10" height="13" viewBox="0 0 10 13" aria-hidden="true"><path d="M5 0a5 5 0 0 0-5 5c0 4 5 8 5 8s5-4 5-8a5 5 0 0 0-5-5zm0 7a2 2 0 1 1 0-4 2 2 0 0 1 0 4z" fill="#fff"/></svg>
      Unit 4, 12 Ridgeline Place, Ashvale NSW 2190
    </div>
    <div class="contact-band__links">
      <span>&#9993; dferrant@strucovadc.com.au</span>
      <span>&#9675; www.strucovadc.com.au</span>
    </div>
  </div>

  <div class="badges">
    <div class="badge" role="img" aria-label="Energy rating partner badge"></div>
    <div class="badge badge--round" role="img" aria-label="Professional engineering body badge"></div>
  </div>
</section>

<section class="page page--cover">
  <div class="cover-band"></div>
  <p class="cover-web">www.strucovadc.com.au</p>

  <div class="photo-strip">
    <div class="photo" style="background:linear-gradient(180deg,#c9ced3,#8e969e)" role="img" aria-label="Photo of rooftop ductwork"></div>
    <div class="photo" style="background:linear-gradient(180deg,#b9c0c6,#7d858c)" role="img" aria-label="Photo of electrical switchboard room"></div>
    <div class="photo" style="background:linear-gradient(180deg,#9eb5c8,#2f3a45)" role="img" aria-label="Photo of pumps and pipework"></div>
    <div class="photo" style="background:linear-gradient(180deg,#d8d6d2,#b84a40)" role="img" aria-label="Photo of red fire sprinkler pipes"></div>
  </div>

  <svg class="swoosh" viewBox="0 0 540 130" preserveAspectRatio="none" aria-hidden="true">
    <path d="M0 20 Q270 70 540 10 L540 130 L0 130 Z" fill="#abd036"/>
    <path d="M0 110 Q300 80 540 40 L540 130 L0 130 Z" fill="#f4f4f4"/>
  </svg>

  <div class="brand">
    <div class="brand__mark"></div>
    <div class="brand__name">STRUCOVA<br>DESIGN</div>
  </div>
  <div class="abn">ABN 41 702 558 903</div>

  <div class="cover-heading">
    <div class="cover-heading__main">BUILDING</div>
    <div class="cover-heading__sub">SERVICES CONSULTANTS</div>
  </div>
  <ul class="services">
    <li>MECHANICAL</li>
    <li>ELECTRICAL</li>
    <li>HYDRAULIC</li>
    <li>WET / DRY FIRE</li>
    <li>BUILDING ENERGY EFFICIENCY</li>
  </ul>
</section>

</body>
</html>
```